Email signature design - law firm

We are a small boutique law firm which is located near the beach in Manly, Australia.

We have just recently developed a new logo and are looking to redesign our letterhead, business cards and email signatures.

This brief is for our email signatures. This is an email signature to appear at the bottom of our Outlook emails so we would like it to be text that we are able to edit as the wording in our email signature often required amendments.

I have attached a word document which had our new logo, and our previous email signature which all the information/wording that needs to be included.

We would like multiple designs with a modern, simplistic yet striking look.

Thanks.

font - raleway or montserrat
Updates

Colors

Designer to choose colors to be used in the design.

Requirements
Must have
• Must have the exact wording which appears in the email signature in the word document attached to brief.
• Must be able to edit the text as it is for an Outlook email signature which wording will change from time to time.

```html
<!DOCTYPE html>
<html lang="en">
<head>
<meta charset="utf-8">
<title>Corwell &amp; Partners – Email Signature</title>
<link href="https://fonts.googleapis.com/css2?family=Raleway:wght@400;500;700&display=swap" rel="stylesheet">
<style>
  :root {
    --ink: #1d1d1f;
    --muted: #6e6e73;
    --accent: #6b7fc2;
    --link: #3b4aa0;
    --placeholder: #e6e7e9;
    --rule: #dcdcdc;
    --paper: #ffffff;
  }
  * { box-sizing: border-box; margin: 0; padding: 0; }
  html, body {
    width: 754px; height: 1200px; overflow: hidden;
    background: var(--paper);
    font-family: "Raleway", sans-serif;
    color: var(--ink);
  }
  .email { position: relative; width: 754px; height: 1200px; }

  .greeting { position: absolute; left: 63px; top: 60px; font-size: 17px; }

  .message-body { position: absolute; left: 62px; top: 102px; width: 638px; }
  .message-line { height: 22px; background: var(--placeholder); margin-bottom: 9.6px; }
  .message-line--short { width: 334px; }

  .sign-off { position: absolute; left: 63px; top: 386px; font-size: 17px; line-height: 22px; }

  .signature { position: absolute; left: 56px; top: 472px; width: 632px; height: 136px; }
  .brand-mark {
    position: absolute; left: 0; top: 0; width: 226px; height: 136px;
    display: flex; align-items: center; justify-content: center; gap: 8px;
  }
  .brand-mark__dot { width: 14px; height: 14px; border-radius: 50%; background: var(--accent); }
  .brand-mark__name { font-size: 17px; font-weight: 700; color: var(--link); letter-spacing: 0.5px; }
  .signature__divider { position: absolute; left: 226px; top: 0; width: 1px; height: 136px; background: var(--rule); }
  .contact { position: absolute; left: 269px; top: 10px; font-size: 17.5px; line-height: 22px; color: var(--muted); }
  .contact__firm { color: var(--ink); font-weight: 700; }
  .contact__web { color: var(--link); text-decoration: none; }

  .footer-rule { position: absolute; left: 56px; top: 628px; width: 632px; height: 1px; background: var(--rule); }

  .notices { position: absolute; left: 56px; top: 666px; width: 637px; font-size: 17px; line-height: 22px; }
  .notice { margin-bottom: 22px; }
  .notice__title { color: var(--accent); font-weight: 700; }
  .notice p { text-align: justify; hyphens: auto; }
</style>
</head>
<body>
<main class="email">
  <p class="greeting">Dear Maren,</p>

  <div class="message-body" aria-label="Message text">
    <div class="message-line"></div>
    <div class="message-line"></div>
    <div class="message-line"></div>
    <div class="message-line"></div>
    <div class="message-line"></div>
    <div class="message-line"></div>
    <div class="message-line"></div>
    <div class="message-line"></div>
    <div class="message-line message-line--short"></div>
  </div>

  <p class="sign-off">Regards,<br>Tessa Holloway</p>

  <section class="signature">
    <div class="brand-mark">
      <span class="brand-mark__dot"></span>
      <span class="brand-mark__name">Corwell &amp; Partners</span>
    </div>
    <div class="signature__divider"></div>
    <div class="contact">
      <div class="contact__firm">Corwell &amp; Partners</div>
      <div>Suite 4, 18 Harbour Lane, COVEBAY&nbsp; NSW&nbsp; 2999</div>
      <div>Ph: (02) 5550 1840</div>
      <div>Fax: (02) 5550 1841</div>
      <a class="contact__web" href="#">www.corwellpartners.com.au</a>
    </div>
  </section>

  <div class="footer-rule"></div>

  <section class="notices">
    <div class="notice">
      <div class="notice__title">Important note:</div>
      <p>This E-Mail and any attachment is PRIVILEGED and confidential.&nbsp; It must not be read, copied, disclosed or used by any person other than the above named addressees.&nbsp; In order to preserve the intended confidentiality and privilege, please notify us immediately if you have received this e-mail by mistake and secure-delete this e-mail from your system.</p>
      <p>Unauthorised perusal, use, disclosure, forwarding or copying is strictly prohibited and may be unlawful.</p>
    </div>
    <div class="notice">
      <p>Liability limited by a scheme approved under Professional Standards Legislation. Legal practitioners at CoveLaw (NSW) Pty Ltd are members of the scheme.</p>
    </div>
    <div class="notice">
      <div class="notice__title">Fraud warning:</div>
      <p>Please be aware that there is a significant risk posed by cyber fraud, specifically relating to email accounts and bank account details. Our bank account details will never change during the course of a transaction, and we will never advise you of a change to our bank details via email.&nbsp; Please check account details with us in person or by phone before making payments.&nbsp; If you advise us of your bank account details by email, please also ring and confirm the bank account details by phone as well.</p>
    </div>
  </section>
</main>
</body>
</html>
```